Breakfast Voucher in Business Card Form

I need a breakfast voucher produced on a business card format 85mm x 54mm with rounded corners. 3mm internal and external bleed.

Attach are logos and text required.

Id like this to be easy to ready but also looks smart with plenty of colour.

Font styles to use
Sans Serif

Colors
33a6d7
ffffff
ec1f27
000000

```html
<!DOCTYPE html>
<html lang="en">
<head>
<meta charset="utf-8">
<title>Breakfast Discount Voucher</title>
<link rel="stylesheet" href="https://fonts.googleapis.com/css2?family=Archivo+Black&family=Arimo:wght@400;700&display=swap">
<style>
  :root {
    --cyan: #5fe3ea;
    --red: #ec1f27;
    --black: #000000;
    --white: #ffffff;
    --rule: #8a8a8a;
    --edge: #d6d6d6;
    --plate: #efeeec;
    --salmon: #e9876a;
    --salmon-soft: #eeb39f;
  }
  * { margin: 0; padding: 0; box-sizing: border-box; }
  html, body { width: 1200px; height: 374px; overflow: hidden; background: var(--white); }
  .sheet { position: relative; width: 1200px; height: 374px; }
  .card {
    position: absolute; top: 0; width: 588px; height: 374px;
    border: 1px solid var(--edge); background: var(--white); overflow: hidden;
  }
  .card--front { left: 0; }
  .card--back { left: 612px; }
  .card svg.shapes { position: absolute; inset: 0; }
  .brand-name {
    position: absolute; left: 30px; top: 72px;
    font-family: "Arimo", sans-serif; font-weight: 700; font-size: 24px;
    color: var(--black); letter-spacing: 0.3px;
  }
  .headline {
    position: absolute;
    font-family: "Archivo Black", sans-serif; color: var(--cyan);
    line-height: 1; transform: skewX(-10deg) scaleX(0.85); transform-origin: left bottom;
    white-space: nowrap;
  }
  .card--front .headline { font-size: 34px; }
  .card--back .headline { font-size: 30px; }
  .valid-at {
    position: absolute; display: flex; align-items: baseline; gap: 8px;
    font-family: "Arimo", sans-serif; color: var(--black); white-space: nowrap;
  }
  .venue-name { font-family: "Arimo", sans-serif; font-weight: 400; color: var(--red); }
  .card--front .valid-at { left: 170px; top: 290px; font-size: 16px; }
  .card--front .venue-name { font-size: 20px; }
  .card--back .valid-at { left: 276px; top: 305px; font-size: 16px; }
  .card--back .venue-name { font-size: 30px; }
  .offer {
    position: absolute; left: 276px; top: 156px;
    font-family: "Arimo", sans-serif; font-size: 16.5px; line-height: 20px; color: var(--black);
  }
  .validity {
    position: absolute; left: 276px; top: 262px;
    font-family: "Arimo", sans-serif; font-size: 16px; color: var(--black);
    display: flex; align-items: flex-end;
  }
  .validity .blank { display: inline-block; width: 178px; border-bottom: 1px solid var(--black); margin-left: 3px; height: 16px; }
</style>
</head>
<body>
<div class="sheet">

  <section class="card card--front">
    <svg class="shapes" width="588" height="374" viewBox="0 0 588 374">
      <defs>
        <radialGradient id="dishFront" cx="0.62" cy="0.55" r="0.55">
          <stop offset="0" stop-color="var(--salmon)"/>
          <stop offset="0.45" stop-color="#efc09f"/>
          <stop offset="1" stop-color="var(--plate)"/>
        </radialGradient>
      </defs>
      <polygon role="img" aria-label="Photo of smoked salmon eggs benedict on toasted muffins"
               points="240,0 588,0 588,374 380,374" fill="url(#dishFront)"/>
      <line class="edge-dots" x1="240" y1="0" x2="380" y2="374" stroke="var(--rule)" stroke-width="1" stroke-dasharray="2 2"/>
      <polygon class="accent-band" points="240,0 488,0 262,34" fill="var(--red)"/>
      <polygon class="accent-band" points="0,312 364,312 380,352 0,352" fill="var(--red)"/>
      <line class="title-rule" x1="12" y1="210" x2="318" y2="190" stroke="var(--rule)" stroke-width="1" stroke-dasharray="2 2"/>
    </svg>
    <div class="brand-name">Skyward Ballooning</div>
    <div class="headline" style="left:30px; top:164px;">Breakfast</div>
    <div class="headline" style="left:34px; top:206px;">Discount Voucher</div>
    <div class="valid-at">Valid at <span class="venue-name">Copperleaf</span></div>
  </section>

  <section class="card card--back">
    <svg class="shapes" width="588" height="374" viewBox="0 0 588 374">
      <defs>
        <radialGradient id="dishBack" cx="0.5" cy="0.5" r="0.6">
          <stop offset="0" stop-color="var(--salmon-soft)"/>
          <stop offset="0.5" stop-color="#f2d2c2"/>
          <stop offset="1" stop-color="var(--plate)"/>
        </radialGradient>
      </defs>
      <rect role="img" aria-label="Faded photo of smoked salmon eggs benedict"
            x="0" y="0" width="254" height="374" fill="url(#dishBack)"/>
      <line class="title-rule" x1="236" y1="102" x2="564" y2="80" stroke="var(--rule)" stroke-width="1" stroke-dasharray="2 2"/>
    </svg>
    <div class="headline" style="left:276px; top:60px;">Breakfast</div>
    <div class="headline" style="left:278px; top:98px;">Discount Voucher</div>
    <p class="offer">Present at Copperleaf Restaurant<br>to receive your full buffet breakfast at<br>our special discounted price</p>
    <div class="validity">Valid:<span class="blank"></span></div>
    <div class="valid-at">Valid at <span class="venue-name">Copperleaf</span></div>
  </section>

</div>
</body>
</html>
```